Coffee distributor in London website concept design

We have just launched a rebranded coffee distributor in London supplying coffee to bars, restaurants, coffee shops and hotels.

We sell coffee, coffee machines, barista training and work with 2 brands - Valdorini and Ruzzo. We want the site to have calls to action (i.e. advertising boxes that promote something such as a new blend or machine.

The site should be focused towards foodservice clients such as those mentioned above, and should follow the colours of the logo (the current site is www.brunotto42.com). There should be around 200 - 250 words on the home page, and should make us look professional, modern, knowledgeable and most importantly, unique.

Sites to look at:
http://www.tallowbeans.com/
http://www.pellbrookcup.com/
http://www.greenlanternbrew.com/
http://www.corwinhastley.com/
http://www.velmarouk.com/
http://www.quarryroasted.com/
http://www.fernitebrew.co.uk/
http://www.tazzinobrew.co.uk/
http://www.valdorini.it/en/
http://www.ruzzo.co.uk/
Updates

Just a quick reminder, we are a coffee distributor/wholesaler, not a coffee shop.

Some sites to look Sites to look at:
http://www.velmarouk.com/
http://www.ruzzo.co.uk/at:

Target Market(s)

We are targeting businesses, and will be using SEO and social media to be found. Our target customers are restaurants, coffee shops, hotels, pubs and bars.

Industry/Entity Type

Advertising

Font styles to use
Sans Serif

Colors
ec1f27

Requirements
Must have
• The home page, and maybe inner pages to a lesser extent, should have a banner which changes, and some advertising boxes (look at http://www.corwinhastley.com for example).

There should also be a minimum of 200 words on a page.

We currently have a Facebook page, but will be looking to launch Instagram, twitter, YouTube and Google+, so there should be icons (ideally branded in our colour scheme and look) which link to these pages.

```html
<!DOCTYPE html>
<html lang="en">
<head>
<meta charset="utf-8">
<title>Brunotto42 – Coffee Distributors</title>
<link rel="stylesheet" href="https://fonts.googleapis.com/css2?family=Text+Me+One&family=Didact+Gothic&display=swap">
<style>
:root{
  --brand-red:#bb2d2f;
  --dark-panel:#251c1b;
  --footer-bg:#231b1a;
  --cream:#fdf9e1;
  --white:#ffffff;
  --bean-dark:#120a07;
  --bean-mid:#3a2418;
}
*{box-sizing:border-box;margin:0;padding:0}
html,body{width:1200px;height:807px;overflow:hidden}
body{position:relative;font-family:"Didact Gothic",sans-serif;color:var(--white);background:var(--footer-bg)}
a{color:inherit;text-decoration:none}

.site-header{position:absolute;left:0;top:0;width:1200px;height:75px;background:var(--brand-red)}
.brand-logo{position:absolute;left:100px;top:0;width:130px;height:75px;background:var(--white);display:flex;align-items:center;justify-content:center;color:var(--brand-red);font-size:22px}
.main-nav{position:absolute;left:261px;top:24px;display:flex;gap:38px;font-size:18px;line-height:22px}
.main-nav .has-menu::after{content:"";display:inline-block;width:6px;height:6px;border-right:2px solid var(--white);border-bottom:2px solid var(--white);transform:rotate(45deg);margin-left:8px;position:relative;top:-4px}
.social-list{position:absolute;display:flex;gap:11px;list-style:none}
.site-header .social-list{left:935px;top:25px}
.social-list li{width:24px;height:24px;border-radius:50%;background:var(--white)}

.stage{position:absolute;left:0;top:75px;width:1200px;height:560px;background:radial-gradient(ellipse at 20% 30%,var(--bean-mid),var(--bean-dark) 60%),var(--bean-dark)}
.stage-bg{position:absolute;inset:0;background:radial-gradient(circle at 80% 70%,rgba(70,42,28,.55),transparent 45%),radial-gradient(circle at 10% 85%,rgba(70,42,28,.5),transparent 40%)}

.hero{position:absolute;left:100px;top:20px;width:1000px;height:282px;background:var(--dark-panel)}
.hero-title{position:absolute;left:24px;top:6px;width:515px;font-family:"Text Me One",sans-serif;font-size:56px;line-height:50px;font-weight:400;color:var(--cream);letter-spacing:1px;-webkit-text-stroke:1.2px var(--cream)}
.hero-text{position:absolute;left:27px;top:167px;width:470px;font-size:11.5px;line-height:14px;text-transform:uppercase;color:var(--cream);letter-spacing:-.1px}
.hero-dots{position:absolute;left:27px;top:252px;display:flex;gap:10px;list-style:none}
.hero-dots li{width:10px;height:10px;border-radius:50%;background:var(--cream)}
.hero-dots li.is-active{background:var(--brand-red)}
.hero-photo{position:absolute;left:543px;top:0;width:457px;height:282px;background:linear-gradient(180deg,#2a1d17 0%,#5a3a27 45%,#b89a7a 80%,#8d6f58 100%)}
.hero-strip{position:absolute;left:100px;top:302px;width:1000px;height:18px;background:var(--cream)}

.promo{position:absolute;top:340px;width:320px;height:200px;background:var(--dark-panel)}
.promo-title{position:absolute;left:20px;top:16px;font-size:17px;line-height:20px;font-weight:400;text-transform:uppercase}
.promo-photo{position:absolute;left:20px;top:48px;width:140px;height:102px}
.promo-text{position:absolute;left:173px;top:50px;width:140px;font-size:12px;line-height:14px;text-transform:uppercase}
.promo-cta{position:absolute;left:0;bottom:0;width:320px;height:30px;background:var(--brand-red);text-align:right;padding-right:10px;font-size:17px;line-height:30px;text-transform:uppercase}
.promo--coffees{left:100px}
.promo--coffees .promo-photo{background:linear-gradient(135deg,#d9b08a,#f3ece4 50%,#c48a5c)}
.promo--machines{left:440px}
.promo--machines .promo-title{left:18px}
.promo--machines .promo-photo{width:108px;background:linear-gradient(180deg,#ffffff,#b9b9b9 60%,#5a5a5a)}
.promo--machines .promo-text{left:178px;width:132px}
.promo--brands{left:780px}
.brand-names{position:absolute;left:20px;top:86px;width:280px;display:flex;justify-content:space-between;align-items:center;font-size:26px}

.site-footer{position:absolute;left:0;top:635px;width:1200px;height:172px;background:var(--footer-bg)}
.footer-heading{font-size:19px;font-weight:400;margin-bottom:6px;line-height:22px}
.quick-links{position:absolute;left:100px;top:18px}
.quick-links ul{list-style:none;font-size:13.5px;line-height:16px}
.footer-contact{position:absolute;left:500px;top:18px}
.footer-contact .social-list{position:static;margin-top:10px}
.footer-brand{position:absolute;right:100px;top:14px;text-align:right;font-size:14px;line-height:18px}
.footer-logo{color:var(--brand-red);font-size:32px;line-height:44px;margin-bottom:25px}
.footer-rule{position:absolute;left:100px;top:130px;width:1000px;height:1px;background:var(--brand-red)}
.copyright{position:absolute;right:100px;top:142px;font-size:12.5px}
</style>
</head>
<body>
<header class="site-header">
  <a class="brand-logo" href="#">Brunotto42</a>
  <nav class="main-nav">
    <a class="has-menu" href="#">Coffees</a>
    <a class="has-menu" href="#">Machines</a>
    <a href="#">Barista Training</a>
    <a href="#">About us</a>
    <a href="#">Contact</a>
  </nav>
  <ul class="social-list" aria-label="Social profiles">
    <li aria-label="Social profile"></li><li aria-label="Social profile"></li><li aria-label="Social profile"></li><li aria-label="Video channel"></li><li aria-label="Photo profile"></li>
  </ul>
</header>

<main class="stage">
  <div class="stage-bg" role="img" aria-label="Close-up of roasted coffee beans"></div>

  <section class="hero">
    <h1 class="hero-title">DO YOU NEED HELP WITH YOUR COFFEE SHOP?</h1>
    <p class="hero-text">Nulla metus metus, ullamcorper vel, tincidunt sed, euismod in, nibh. Quisque volutpat condimentum velit. Class aptent taciti sociosqu ad litora torquent per conubia nostra, per inceptos himenaeos. Nam nec ante.</p>
    <ul class="hero-dots"><li class="is-active"></li><li></li><li></li></ul>
    <div class="hero-photo" role="img" aria-label="Interior of a coffee shop with wooden bar stools and shelves"></div>
  </section>
  <div class="hero-strip"></div>

  <article class="promo promo--coffees">
    <h2 class="promo-title">Try our new coffees</h2>
    <div class="promo-photo" role="img" aria-label="Cappuccino with latte art on a saucer"></div>
    <p class="promo-text">Integer nec odio. Praesent libero. Sed cursus ante dapibus diam. Sed nisi. Nulla quis sem at nibh elementum imperdiet.</p>
    <a class="promo-cta" href="#">Choose your favorite</a>
  </article>

  <article class="promo promo--machines">
    <h2 class="promo-title">Machines categories</h2>
    <div class="promo-photo" role="img" aria-label="Stainless steel espresso machine"></div>
    <p class="promo-text">Class aptent taciti sociosqu ad litora torquent per conubia nostra, per inceptos himenaeos. Curabitur sodales ligula in libero.</p>
    <a class="promo-cta" href="#">Browse the latest machines</a>
  </article>

  <article class="promo promo--brands">
    <h2 class="promo-title">Authorised London and<br>South-East distributors of</h2>
    <div class="brand-names"><span>Ruzzo</span><span>Valdorini</span></div>
    <a class="promo-cta" href="#">Read more</a>
  </article>
</main>

<footer class="site-footer">
  <div class="quick-links">
    <h3 class="footer-heading">Quick links</h3>
    <ul>
      <li><a href="#">Browse Coffees</a></li>
      <li><a href="#">Browse Machines</a></li>
      <li><a href="#">Barista Training</a></li>
    </ul>
  </div>
  <div class="footer-contact">
    <h3 class="footer-heading">Contact us</h3>
    <ul class="social-list" aria-label="Social profiles">
      <li aria-label="Social profile"></li><li aria-label="Social profile"></li><li aria-label="Social profile"></li><li aria-label="Video channel"></li><li aria-label="Photo profile"></li>
    </ul>
  </div>
  <div class="footer-brand">
    <p class="footer-logo">Brunotto42</p>
    <p>020 7946 0381</p>
    <p>info@brunotto42.com</p>
  </div>
  <div class="footer-rule"></div>
  <p class="copyright">Copyright 2013 Brunotto42, All Rights Reserved</p>
</footer>
</body>
</html>
```